Re-Design of existing Shopify Website

Hi,

We are looking for a skilled person to work with us on improving the design of our website to make it more user friendly. We are a Makeup brush and makeup accessories company and our current website can be viewed at tinkpetalco dot com.We are looking to simplify the layout and make it more modern and mobile friendly.

We have designs in mind which we would like to implement to our site which we feel would work better for us to increase traffic and sales.

We would like the layout to have clear sections for brushes,lashes ,sponge and also our tutorials on the landing page.

Industry/Entity Type

Hair And Beauty

Number of Pages Required

5+ page

Font styles to use
Sans Serif

Colors
b8a6cd
d3a5cc
eea4c8
ffffff
000000

Requirements
Must have
• -Clear ,modern landing page.
• -easy navigation
• -simple design
• -professional design approach
Nice to have
• cross selling pop up
Should not have
• over use of bold colour.

```html
<!DOCTYPE html>
<html lang="en">
<head>
<meta charset="utf-8">
<title>Tink Petal Co – Makeup Brushes &amp; Accessories</title>
<link href="https://fonts.googleapis.com/css2?family=Open+Sans:wght@400;600;700&display=swap" rel="stylesheet">
<style>
  :root {
    --pink: #e0488f;
    --pink-soft: #d46a9b;
    --rose-icon: #b87a88;
    --ink: #333333;
    --white: #ffffff;
    --peach-bg: #fde9e0;
    --sand-bg: #ede4de;
    --footer-bg: #4a4545;
    --footer-text: #e6e0e0;
    --field-line: #d8d2d2;
  }
  * { box-sizing: border-box; margin: 0; padding: 0; }
  html, body { width: 1200px; height: 2844px; overflow: hidden; }
  body { font-family: "Open Sans", Arial, sans-serif; color: var(--ink); background: var(--white); position: relative; }
  .abs { position: absolute; }

  /* Hero */
  .hero { position: absolute; left: 0; top: 0; width: 1200px; height: 684px; overflow: hidden; }
  .hero-photo { position: absolute; inset: 0;
    background: radial-gradient(ellipse 420px 520px at 900px 260px, #c8a595 0%, #8a6f68 35%, rgba(60,64,80,0) 75%),
                linear-gradient(100deg, #38465a 0%, #2c3646 45%, #3a3c48 100%); }
  .brand { position: absolute; left: 86px; top: 38px; display: flex; align-items: center; gap: 14px; }
  .brand-mark { width: 22px; height: 22px; border-radius: 50%; background: var(--pink); }
  .brand-name { font-size: 30px; font-weight: 600; color: var(--white); letter-spacing: 1px; }
  .main-nav { position: absolute; right: 87px; top: 37px; display: flex; gap: 34px; }
  .main-nav a { color: var(--white); text-decoration: none; font-size: 17px; text-transform: uppercase; }
  .main-nav a.active { color: var(--pink); }
  .hero-title { position: absolute; left: 86px; top: 259px; width: 640px; color: var(--white); font-size: 40px; font-weight: 600; line-height: 46px; }
  .hero-title .last { display: block; margin-top: 16px; }
  .btn-outline-light { position: absolute; left: 87px; top: 467px; width: 206px; height: 69px; border: 4px solid var(--white); color: var(--white); font-size: 24px; font-weight: 600; display: flex; align-items: center; justify-content: center; }
  .slider-dots { position: absolute; left: 571px; top: 640px; display: flex; gap: 14px; }
  .slider-dots span { width: 17px; height: 17px; border-radius: 50%; border: 3px solid var(--white); }
  .slider-dots span.on { background: var(--white); }

  /* About */
  .section-title { color: var(--pink); font-size: 31px; font-weight: 400; text-transform: uppercase; }
  .about-title { left: 86px; top: 735px; }
  .about-text { left: 86px; top: 791px; width: 1010px; font-size: 22px; line-height: 40px; }
  .btn-outline-pink { position: absolute; border: 2px solid var(--pink-soft); color: var(--pink); display: flex; align-items: center; justify-content: center; text-transform: uppercase; }
  .about-btn { left: 89px; top: 944px; width: 184px; height: 51px; font-size: 22px; }

  /* Range cards */
  .range { position: absolute; top: 1049px; height: 600px; }
  .range.brushes { left: 0; width: 607px; background: var(--peach-bg); }
  .range.lashes { left: 607px; width: 593px; background: var(--sand-bg); }
  .range h3 { position: absolute; top: 26px; color: var(--pink); font-size: 24px; font-weight: 400; }
  .range-photo { position: absolute; top: 86px; height: 298px; }
  .range p { position: absolute; top: 417px; font-size: 19px; line-height: 27px; width: 440px; }
  .price { position: absolute; top: 502px; width: 153px; height: 42px; border: 2px solid var(--pink-soft); color: var(--pink); font-size: 22px; display: flex; align-items: center; justify-content: center; }

  /* Features */
  .feature { position: absolute; top: 1690px; width: 320px; height: 320px; }
  .feature svg { position: absolute; left: 0; top: 0; width: 72px; height: 74px; }
  .feature h4 { position: absolute; left: 0; top: 102px; color: var(--pink); font-size: 22px; font-weight: 400; line-height: 30px; white-space: nowrap; }
  .feature p { position: absolute; left: 0; top: 157px; font-size: 19px; line-height: 27px; width: 290px; }
  .feature .btn-outline-pink { left: 0; top: 270px; width: 155px; height: 42px; font-size: 19px; }

  /* Contact */
  .contact { position: absolute; left: 0; top: 2056px; width: 1200px; height: 722px; overflow: hidden; }
  .contact-photo { position: absolute; inset: 0;
    background: radial-gradient(ellipse 300px 500px at 870px 380px, #6e6262 0%, #463a3b 45%, rgba(42,34,35,0) 80%),
                linear-gradient(90deg, #2a2223 0%, #342b2c 60%, #3a3031 100%); }
  .contact-title { position: absolute; left: 86px; top: 36px; color: var(--white); font-size: 34px; font-weight: 600; text-transform: uppercase; }
  .field-label { position: absolute; color: var(--white); font-size: 25px; font-weight: 600; text-transform: uppercase; line-height: 34px; }
  .field { position: absolute; border: 4px solid var(--field-line); background: rgba(255,255,255,0.03); }
  .btn-send { position: absolute; left: 87px; top: 626px; width: 231px; height: 53px; border: 4px solid var(--white); color: var(--white); font-size: 24px; font-weight: 600; display: flex; align-items: center; justify-content: center; text-transform: uppercase; }

  /* Footer */
  .site-footer { position: absolute; left: 0; top: 2778px; width: 1200px; height: 66px; background: var(--footer-bg); display: flex; align-items: center; justify-content: space-between; padding: 0 86px 0 86px; }
  .site-footer small { color: var(--footer-text); font-size: 21px; }
  .contact-icons { display: flex; gap: 28px; align-items: center; }
  .contact-icons svg { width: 22px; height: 22px; display: block; }
</style>
</head>
<body>

<header class="hero">
  <div class="hero-photo" role="img" aria-label="Model with long flowing wavy hair and full makeup against a dark blue studio backdrop"></div>
  <div class="brand">
    <span class="brand-mark"></span>
    <span class="brand-name">Tink Petal Co</span>
  </div>
  <nav class="main-nav">
    <a class="active" href="#">Home</a>
    <a href="#">Brushes</a>
    <a href="#">Lashes</a>
    <a href="#">Sponges</a>
    <a href="#">Tutorials</a>
    <a href="#">Contact</a>
  </nav>
  <h1 class="hero-title">QUALITY BEAUTY : A unique<br>solution for Your<span class="last">Hair &amp; Beauty.</span></h1>
  <div class="btn-outline-light">CONTACT NOW</div>
  <div class="slider-dots"><span class="on"></span><span></span><span></span></div>
</header>

<section>
  <h2 class="section-title abs about-title">About Us</h2>
  <p class="abs about-text">Lorem Ipsum is simply dummy text of the printing and typesetting industry. Lorem Ipsum has been the industry's standard dummy text ever since the 1500s, when an unknown printer took a galley of type and scrambled it to make a type specimen book.</p>
  <div class="btn-outline-pink about-btn">Know More</div>
</section>

<section>
  <article class="range brushes">
    <h3 style="left:86px">Makeup Brushes</h3>
    <div class="range-photo" style="left:87px;width:457px;background:linear-gradient(120deg,#e4dcd6 0%,#c9a58a 45%,#8f6b55 100%)" role="img" aria-label="Set of soft makeup brushes in a blush tone"></div>
    <p style="left:86px">Lorem Ipsum is simply dummy text of the printing and typesetting industry.</p>
    <div class="price" style="left:87px">$56.10</div>
  </article>
  <article class="range lashes">
    <h3 style="left:69px">Lashes</h3>
    <div class="range-photo" style="left:69px;width:435px;background:linear-gradient(110deg,#3c4a6a 0%,#8b7566 40%,#d7b8a2 70%,#2e4a86 100%)" role="img" aria-label="Pairs of false eyelashes on a soft background"></div>
    <p style="left:69px">Lorem Ipsum is simply dummy text of the printing and typesetting industry.</p>
    <div class="price" style="left:70px">$56.10</div>
  </article>
</section>

<section>
  <div class="feature" style="left:87px">
    <svg viewBox="0 0 40 40" aria-hidden="true"><path d="M20 4C13 12 8 19 8 25a12 12 0 0 0 24 0c0-6-5-13-12-21z" fill="var(--rose-icon)"/><ellipse cx="15" cy="25" rx="2.5" ry="4" fill="#fff" opacity=".6"/></svg>
    <h4>Beauty Sponges</h4>
    <p>Morbi interdum mollis sapien. Sed ac risus. Phasellus lacinia, magna lorem ullamcorper.</p>
    <div class="btn-outline-pink">Know More</div>
  </div>
  <div class="feature" style="left:469px">
    <svg viewBox="0 0 40 40" aria-hidden="true"><circle cx="20" cy="20" r="16" fill="none" stroke="var(--rose-icon)" stroke-width="3"/><path d="M16 13v14l11-7z" fill="var(--rose-icon)"/></svg>
    <h4>Tutorials</h4>
    <p>Morbi interdum mollis sapien. Sed ac risus. Phasellus lacinia, magna lorem ullamcorper.</p>
    <div class="btn-outline-pink">Know More</div>
  </div>
  <div class="feature" style="left:836px">
    <svg viewBox="0 0 40 40" aria-hidden="true"><rect x="12" y="2" width="10" height="6" fill="var(--rose-icon)"/><rect x="6" y="10" width="22" height="28" rx="4" fill="var(--rose-icon)"/><rect x="10" y="18" width="14" height="10" fill="#fff"/><path d="M30 36c-6-4-2-12 6-12 1 6-2 12-6 12z" fill="var(--rose-icon)"/></svg>
    <h4>Quality Products</h4>
    <p>Morbi interdum mollis sapien. Sed ac risus. Phasellus lacinia, magna lorem ullamcorper.</p>
    <div class="btn-outline-pink">Know More</div>
  </div>
</section>

<section class="contact">
  <div class="contact-photo" role="img" aria-label="Model with short hair in denim sitting on a red stool in a dark studio"></div>
  <h2 class="contact-title">Get In Touch</h2>
  <span class="field-label" style="left:87px;top:109px">Name</span>
  <div class="field" style="left:87px;top:173px;width:486px;height:69px"></div>
  <span class="field-label" style="left:627px;top:109px">Email</span>
  <div class="field" style="left:627px;top:173px;width:486px;height:69px"></div>
  <span class="field-label" style="left:87px;top:276px">Message</span>
  <div class="field" style="left:87px;top:340px;width:1026px;height:235px"></div>
  <div class="btn-send">Send Message</div>
</section>

<footer class="site-footer">
  <small>@2018. All Rights Reserved</small>
  <div class="contact-icons" aria-label="Contact links">
    <svg viewBox="0 0 24 24" aria-label="Email"><rect x="2" y="5" width="20" height="14" rx="2" fill="none" stroke="var(--pink)" stroke-width="2"/><path d="M3 6l9 7 9-7" fill="none" stroke="var(--pink)" stroke-width="2"/></svg>
    <svg viewBox="0 0 24 24" aria-label="Phone"><path d="M6 3l4 1 1 5-2 1.5a11 11 0 0 0 4.5 4.5L15 13l5 1 1 4-3 3C10 20 4 14 3 6z" fill="var(--footer-text)"/></svg>
    <svg viewBox="0 0 24 24" aria-label="Location"><path d="M12 2a7 7 0 0 0-7 7c0 5 7 13 7 13s7-8 7-13a7 7 0 0 0-7-7z" fill="var(--footer-text)"/><circle cx="12" cy="9" r="2.5" fill="var(--footer-bg)"/></svg>
  </div>
</footer>

</body>
</html>
```